Presentation and Communication Coaching Services Business needs updated interactive web site

I want to keep the color scheme, functionality, and pages of my current site, but with a newer/updated look. I need to improve security and simplify images, etc. (Please see current site http://brackleyvoicementor.com ) This will need be functional on mobile devices, as well.

I'm attached to the scrolling client list and scrolling client feedback.

Industry/Entity Type

Professional Service

Font styles to use
Sans Serif

Colors
0356a4
f37122
33a6d7

Requirements
Must have
• scrolling client banner on home page, client comments slider, color scheme
• Please see current site: http://brackleyvoicementor.com
Nice to have
• better action/appearance
Should not have
• I don't want it to look like all the other sites/templates

```html
<!DOCTYPE html>
<html lang="en">
<head>
<meta charset="utf-8">
<title>Brackley Voice Mentoring</title>
<link href="https://fonts.googleapis.com/css2?family=Questrial&family=Open+Sans:wght@400;600;700&display=swap" rel="stylesheet">
<style>
:root{
  --blue:#0356a4;
  --orange:#f37122;
  --sky:#33a6d7;
  --ink:#222;
  --text:#555;
  --grey:#f1f1f1;
  --dark:#1c1c1e;
  --charcoal:#444;
  --white:#fff;
}
*{box-sizing:border-box;margin:0;padding:0}
html,body{width:1200px;height:4063px;overflow:hidden}
body{font-family:"Open Sans",Arial,sans-serif;color:var(--text);background:var(--white);position:relative}
section,header,footer{position:absolute;left:0;width:1200px;overflow:hidden}

/* hero */
.hero{top:0;height:780px;background:linear-gradient(100deg,#3a2a24 0%,#6b3a22 35%,#8a4b2a 55%,#2c3448 80%,#1d2436 100%)}
.hero-photo{position:absolute;inset:0;background:radial-gradient(circle at 78% 45%,rgba(40,60,110,.85) 0,rgba(30,40,70,.4) 22%,transparent 40%),radial-gradient(circle at 30% 70%,rgba(200,90,40,.35),transparent 50%)}
.nav{position:absolute;top:40px;left:110px;right:110px;display:flex;justify-content:space-between;align-items:center}
.brand{font-family:"Questrial",sans-serif;font-size:24px;color:var(--white);letter-spacing:.3px}
.brand span{color:var(--orange)}
.menu{display:flex;gap:55px;font-size:14px;color:var(--white)}
.menu .on{color:var(--orange)}
.bubble{position:absolute;left:75px;top:165px;width:650px;height:620px;border-radius:50%;background:var(--orange);opacity:.93}
.hero-copy{position:absolute;left:172px;top:258px;width:420px;color:var(--white)}
.hero-copy h1{font-family:"Questrial",sans-serif;font-weight:400;font-size:56px;line-height:66px;white-space:nowrap}
.hero-copy h1 .sky{color:var(--sky)}
.hero-copy p{font-style:italic;font-size:15px;line-height:29px;margin-top:20px}
.hero-copy .who{font-style:normal;font-weight:700;font-size:20px;margin-top:28px}
.hero-copy .who small{font-weight:400;font-size:14px}

/* clients */
.clients{top:780px;height:114px;background:var(--orange);display:flex;align-items:center;justify-content:space-between;padding:0 60px}
.client-row{display:flex;gap:64px;align-items:center;font-family:"Questrial",sans-serif;font-size:28px;color:var(--white);white-space:nowrap}

/* intro */
.intro{top:894px;height:528px}
.intro h2{position:absolute;left:111px;top:70px;font-family:"Questrial",sans-serif;font-weight:400;font-size:32px;color:var(--ink)}
.intro h3{position:absolute;left:111px;top:112px;font-family:"Questrial",sans-serif;font-weight:400;font-size:23px;color:var(--orange)}
.intro p{position:absolute;left:111px;width:440px;font-size:12px;line-height:24px}
.btn{display:inline-block;background:var(--orange);color:var(--white);font-size:16px;padding:13px 30px;border-radius:2px}
.intro .btn{position:absolute;left:111px;top:407px}
.intro .orb{position:absolute;left:880px;top:108px;width:244px;height:244px;border-radius:50%;background:var(--orange)}
.intro .portrait{position:absolute;left:578px;top:60px;width:340px;height:340px;border-radius:50%;background:radial-gradient(circle at 45% 40%,#8a8f95,#3e444b 70%)}

/* pillars */
.pillars{top:1422px;height:339px;background:var(--grey);display:flex;justify-content:center;gap:45px;padding-top:45px}
.pillar{width:205px;text-align:center}
.pillar .ic{width:108px;height:108px;border-radius:50%;margin:0 auto;display:flex;align-items:center;justify-content:center}
.pillar h4{font-family:"Questrial",sans-serif;font-weight:400;font-size:16px;margin-top:14px}
.pillar p{font-size:11.5px;line-height:21px;margin-top:12px}

/* services */
.services{top:1761px;height:623px;background:radial-gradient(ellipse at 50% 20%,#4a3228,#1a1412 75%)}
.sec-title{font-family:"Questrial",sans-serif;font-weight:400;font-size:44px;text-align:center}
.rule{width:58px;height:3px;background:var(--orange);margin:14px auto 0}
.services .sec-title{color:var(--white);margin-top:24px}
.cards{position:absolute;left:111px;top:141px;display:flex;gap:16px}
.card{width:233px;height:414px;background:var(--white);text-align:center}
.card .ph{height:189px}
.card h5{font-family:"Questrial",sans-serif;font-weight:400;font-size:18px;color:var(--ink);margin-top:34px}
.card .rule{width:40px;height:2px;margin-top:10px}
.card p{font-size:11.5px;line-height:21px;margin:14px 20px 0;height:64px}
.card .more{display:inline-block;border:1px solid var(--orange);color:var(--orange);font-size:13px;padding:5px 16px;margin-top:10px}

/* publications */
.pubs{top:2384px;height:542px}
.pubs .sec-title{color:var(--ink);margin-top:50px;font-size:40px}
.tiles{position:absolute;left:111px;top:149px;display:flex;gap:17px}
.tile{width:314px;height:355px;position:relative}
.tile .ph{height:290px}
.tile .cap{position:absolute;left:0;right:0;bottom:0;height:65px;background:var(--blue);color:var(--white);font-size:14px;white-space:nowrap;display:flex;align-items:center;justify-content:center}
.tile.feature .cap{height:140px;background:var(--orange);flex-direction:column;padding:0 20px;text-align:center;white-space:normal}
.tile.feature .cap b{font-family:"Questrial",sans-serif;font-weight:400;font-size:20px}
.tile.feature .cap span{font-size:12px;line-height:22px;margin-top:10px}

/* training */
.training{top:2926px;height:650px}
.training .portrait{position:absolute;left:111px;top:40px;width:550px;height:382px;background:linear-gradient(120deg,#6a4a3a,#b77b58 50%,#3c2a22)}
.panel{position:absolute;left:482px;top:203px;width:629px;height:387px;background:var(--white);border:1px solid #ddd;box-shadow:0 4px 14px rgba(0,0,0,.08);padding:34px 40px}
.panel h3{font-family:"Questrial",sans-serif;font-weight:400;font-size:26px;color:var(--blue);margin-left:-2px}
.panel .rule{margin:10px 0 16px}
.panel ul{list-style:none}
.panel li{font-size:11.5px;line-height:34.5px;color:var(--charcoal);padding-left:36px;position:relative}
.panel li:before{content:"";position:absolute;left:4px;top:13px;width:8px;height:8px;border-radius:50%;background:var(--blue)}

/* testimonials */
.voices{top:3576px;height:292px;background:var(--orange);display:flex;justify-content:center;gap:40px;padding-top:70px}
.voice{display:flex;gap:24px;width:500px}
.voice .badge{flex:none;width:130px;height:130px;border-radius:50%;background:var(--white);border:5px solid #f8b58c;display:flex;align-items:center;justify-content:center;font-family:"Questrial",sans-serif;font-size:19px;color:var(--blue)}
.voice .say{color:var(--white);border-left:1px solid rgba(255,255,255,.5);padding-left:20px}
.voice .say p{font-size:11.5px;line-height:25px}
.voice .say p b{font-family:"Questrial",sans-serif;font-size:26px;opacity:.7;vertical-align:-6px;margin-right:6px}
.voice .by{display:flex;justify-content:space-between;margin-top:12px;font-size:11.5px;line-height:18px}
.voice .by strong{font-weight:700}

/* footer */
.foot{top:3868px;height:195px;background:var(--dark);text-align:center;color:#ccc}
.foot .brand{display:block;font-size:25px;margin-top:30px;color:var(--white)}
.foot .contact{display:flex;justify-content:center;gap:26px;font-size:12.5px;margin-top:30px;color:#ddd}
.foot .contact span{display:flex;align-items:center;gap:8px}
.foot .sep{color:#777}
.foot .copy{font-size:11.5px;margin-top:30px;color:#bbb}
</style>
</head>
<body>

<header class="hero">
  <div class="hero-photo" role="img" aria-label="Photo of a speaker in a suit presenting to a large audience"></div>
  <nav class="nav">
    <div class="brand">brackley<span>voice</span>mentoring</div>
    <div class="menu"><span class="on">Home</span><span>About</span><span>Clients</span><span>Reviews</span><span>Services</span><span>Contact</span></div>
  </nav>
  <div class="bubble"></div>
  <div class="hero-copy">
    <h1>Brackley<br><span class="sky">Voice</span> Mentoring</h1>
    <p>I have taken a number of presentation workshops &amp; I can say far &amp; away that Helena's provided the most useable information, strategies and insights I can't wait to begin to integrate them into my expertise.</p>
    <div class="who">Martin Keele <small>– New York, NY</small></div>
  </div>
</header>

<section class="clients">
  <svg width="24" height="60" viewBox="0 0 24 60"><path d="M20 2 4 30l16 28" stroke="#fff" stroke-width="2" fill="none"/></svg>
  <div class="client-row"><span>Norvia</span><span>Kestrel</span><span>Hale &amp; Wren</span><span>Granmark</span><span>WNX</span><span>Lumera</span></div>
  <svg width="24" height="60" viewBox="0 0 24 60"><path d="M4 2l16 28L4 58" stroke="#fff" stroke-width="2" fill="none"/></svg>
</section>

<section class="intro">
  <h2>You're good at what you do.</h2>
  <h3>Learn How to let it show.</h3>
  <p style="top:165px">An individual works hard to reach a place of respect and authority in her or his chosen profession. Effective self-presentation adds confidence and allows one's unique personality and expertise to shine through – in fact, it is key in separating from the pack and reaching higher goals. As competition increases, these skills are essential in demonstrating value to an employer, market, or board.</p>
  <p style="top:324px">You've done your best to reach this professional level. It's time to develop what it takes to reach the next one.</p>
  <span class="btn">Read More</span>
  <div class="orb"></div>
  <div class="portrait" role="img" aria-label="Photo of a speaker with glasses at a podium microphone"></div>
</section>

<section class="pillars">
  <div class="pillar">
    <div class="ic" style="background:var(--blue)"><svg width="54" height="54" viewBox="0 0 54 54" fill="none" stroke="#fff" stroke-width="3"><circle cx="25" cy="29" r="20"/><circle cx="25" cy="29" r="12"/><circle cx="25" cy="29" r="4" fill="#fff"/><path d="M25 29 47 7M40 7h7v7"/></svg></div>
    <h4 style="color:var(--blue)">The Goal</h4>
    <p>Deliver a focused, engaging message that leads to a successful outcome.</p>
  </div>
  <div class="pillar">
    <div class="ic" style="background:var(--orange)"><svg width="52" height="52" viewBox="0 0 52 52" fill="none" stroke="#fff" stroke-width="3"><path d="M8 14h12a6 6 0 1 1 10 0h12v12a6 6 0 1 0 0 10v10H8V36a6 6 0 1 0 0-10z"/></svg></div>
    <h4 style="color:var(--orange)">The Challenge</h4>
    <p>Find a path to develop skills and strategies to accomplish this aim while also projecting confidence, warmth, and credibility.</p>
  </div>
  <div class="pillar">
    <div class="ic" style="background:var(--sky)"><svg width="52" height="56" viewBox="0 0 52 56" fill="none" stroke="#fff" stroke-width="3"><path d="M18 38c0-6-8-9-8-19a16 16 0 0 1 32 0c0 10-8 13-8 19z"/><path d="M19 44h14M21 50h10"/><path d="M2 19h3M47 19h3M6 4l3 3M46 4l-3 3"/></svg></div>
    <h4 style="color:var(--sky)">The Solution</h4>
    <p>Obtain individualized coaching to grow these necessary skills and establish a reliable strategy to hit the mark every time.</p>
  </div>
  <div class="pillar">
    <div class="ic" style="background:var(--charcoal)"><svg width="44" height="54" viewBox="0 0 44 54" fill="none" stroke="#fff" stroke-width="3"><path d="M3 3h28l10 10v38H3z"/><path d="M11 18h22M11 26h22M11 34h22M11 42h14"/></svg></div>
    <h4 style="color:var(--charcoal)">The Result</h4>
    <p>A natural, confident delivery that comes from knowing what you're doing, how to reach your goal.</p>
  </div>
</section>

<section class="services">
  <h2 class="sec-title">Our Services</h2>
  <div class="rule" style="background:var(--white)"></div>
  <div class="cards">
    <div class="card">
      <div class="ph" role="img" aria-label="Photo of a coach working one-on-one with a client" style="background:linear-gradient(160deg,#6e4a3c,#2b2220)"></div>
      <h5>COACHING</h5><div class="rule"></div>
      <p>One-on-one, individual, &amp; custom coaching to your unique obstacles, &amp; person or via challenges.</p>
      <span class="more">Read More</span>
    </div>
    <div class="card">
      <div class="ph" role="img" aria-label="Photo of a small team workshop around a table" style="background:linear-gradient(160deg,#e9d8cc,#a6765e)"></div>
      <h5>CUSTOM WORKSHOPS</h5><div class="rule"></div>
      <p>Unique, effective program design &amp; facilitation to match the needs of executives, managers.</p>
      <span class="more">Read More</span>
    </div>
    <div class="card">
      <div class="ph" role="img" aria-label="Photo of white figurines facing each other" style="background:linear-gradient(160deg,#4a4a52,#1f1f24)"></div>
      <h5>ACCENTS</h5><div class="rule"></div>
      <p>Support for executives from outside the U.S. to increase intel &amp; diminish obstacles.</p>
      <span class="more">Read More</span>
    </div>
    <div class="card">
      <div class="ph" role="img" aria-label="Photo of a stage microphone close up" style="background:linear-gradient(160deg,#7a7f86,#2a2d33)"></div>
      <h5>KEYNOTE SPEECHES</h5><div class="rule"></div>
      <p>Fresh ways of thinking about speaking and communication combined with practical.</p>
      <span class="more">Read More</span>
    </div>
  </div>
</section>

<section class="pubs">
  <h2 class="sec-title">Recent Publications</h2>
  <div class="rule"></div>
  <div class="tiles">
    <div class="tile">
      <div class="ph" role="img" aria-label="Magazine cover in blue and yellow" style="background:linear-gradient(180deg,#1f8ac9,#e8c22c)"></div>
      <div class="cap">Spring/Summer Dapper Quarterly Style Guide</div>
    </div>
    <div class="tile feature">
      <div class="ph" role="img" aria-label="Magazine cover with a feature article" style="background:linear-gradient(180deg,#8fb4d6,#3e6f9c)"></div>
      <div class="cap"><b>Belle Maison Magazine</b><span>An individual works hard to reach a place of respect &amp; authority in her or his chosen profession.</span></div>
    </div>
    <div class="tile">
      <div class="ph" role="img" aria-label="Photo of a nervous speaker facing press microphones" style="background:linear-gradient(180deg,#b01c1c,#5e0c0c)"></div>
      <div class="cap">Metro Daily Herald</div>
    </div>
  </div>
</section>

<section class="training">
  <div class="portrait" role="img" aria-label="Portrait photo of the coach"></div>
  <div class="panel">
    <h3>BVM Provides Training, Tools, &amp; Techniques</h3>
    <div class="rule"></div>
    <ul>
      <li>Executive Presence – Polishing Personal Presentation/Manner</li>
      <li>Addressing and Overcoming Speaking/Communication Anxiety</li>
      <li>Last-Minute Presentation 911</li>
      <li>Modifying Accents for Clarity and Intelligibility</li>
      <li>Communicating Complex/Technical Material to Any Audience</li>
      <li>Cultivating a More Effective Communication Style</li>
      <li>Incorporating and Interacting with Audio/Visual Aids</li>
      <li>Developing Tools for Dynamic Speaking</li>
    </ul>
  </div>
</section>

<section class="voices">
  <div class="voice">
    <div class="badge">Launchwise</div>
    <div class="say">
      <p><b>“</b>Great communication is really very hard &amp; Helena Brackley is a sherpa of public speaking. So when I first brought Helena in to coach the CEOs of companies in my portfolio, I was impressed.</p>
      <div class="by"><span><strong>OWEN REYES</strong><br>New York, NY</span><span>★★★★★</span></div>
    </div>
  </div>
  <div class="voice">
    <div class="badge">Voltera</div>
    <div class="say">
      <p><b>“</b>Helena was able to understand my needs very quickly and developed a method and a learning process that attended my expectations. She is very experienced in dealing with clients from different regions.</p>
      <div class="by"><span><strong>TIAGO MORAIS</strong><br>Sao Paulo, Brazil</span><span>★★★★★</span></div>
    </div>
  </div>
</section>

<footer class="foot">
  <span class="brand">brackley<span>voice</span>mentoring</span>
  <div class="contact">
    <span><svg width="13" height="13" viewBox="0 0 24 24" fill="#ddd"><path d="M6.6 10.8a15 15 0 0 0 6.6 6.6l2.2-2.2c.3-.3.7-.4 1-.2 1.1.4 2.3.6 3.6.6.6 0 1 .4 1 1V20c0 .6-.4 1-1 1A17 17 0 0 1 3 4c0-.6.4-1 1-1h3.5c.6 0 1 .4 1 1 0 1.3.2 2.5.6 3.6.1.3 0 .7-.2 1z"/></svg>Phone: 555.014.2290</span>
    <span class="sep">|</span>
    <span><svg width="14" height="11" viewBox="0 0 24 18" fill="#ddd"><path d="M0 0h24v18H0zm2 2v.5l10 7 10-7V2z"/></svg>Email: info@brackleyvoicementor.com</span>
    <span class="sep">|</span>
    <span><svg width="11" height="15" viewBox="0 0 16 22" fill="#ddd"><path d="M8 0a8 8 0 0 0-8 8c0 6 8 14 8 14s8-8 8-14a8 8 0 0 0-8-8zm0 11a3 3 0 1 1 0-6 3 3 0 0 1 0 6z"/></svg>43718 Lorem Ipsum Dummy Text Lorem</span>
  </div>
  <div class="copy">© Copyright -2016 Brackley Voice Mentoring. All rights reserved.</div>
</footer>

</body>
</html>
```